Flyer-Design für mobile Bar
Zielgruppe
Wir sind eine Mobile Bar und bieten hochqualitatives Cocktail & Smoothie Catering.
Unsere Zielgruppe sind Unternehmen, insbesondere Messeausteller, Event Agenturen, Eventlokations
Aufgabenstellung
Wir er warten wenig Text, aber aussagekräftige Bilder: auf einer Seite: Cocktails, andere Seite - Smoothies. Format A 5 bzw. für andere ähnliche Formate offen. Auf jeder Seite kommen aufgelistet 5 Optionen ( s.u.) und die Kontaktdaten sowie unser Logo. Spezielle Effekte sind sehr erwünscht ( vergoldet/ Glänzend, Hologram etc.) Wir möchten ein auffallendes modernes Design, des Apetitt auf ein Cocktail/ Smoothie macht.
1. Seite:
Smoothie Bar
Grün
fruchtig
Superfood
detox
Bio
2. Seite:
Cocktailbar
Klassisch
Cocktail LAB
Caipirinha Bar
Cocktail Workshop
Bio Cocktails

```html
<!DOCTYPE html>
<html lang="de">
<head>
<meta charset="utf-8">
<title>Bar Velluto – Flyer</title>
<link rel="stylesheet" href="https://fonts.googleapis.com/css2?family=Roboto:wght@300;400&family=Fira+Sans+Condensed:ital,wght@1,400&display=swap">
<style>
  :root {
    --backdrop: #c8b9ad;
    --page: #000000;
    --text: #ffffff;
    --text-soft: #d9d9d9;
    --caption-shade: rgba(0, 0, 0, 0.72);
  }
  * { margin: 0; padding: 0; box-sizing: border-box; }
  html, body { width: 1200px; height: 1200px; overflow: hidden; }
  body { background: var(--backdrop); position: relative; font-family: "Roboto", sans-serif; }

  .flyer { position: absolute; background: var(--page); color: var(--text); }
  .flyer--front { left: 66px; top: 63px; width: 518px; height: 1040px; }
  .flyer--back { left: 616px; top: 63px; width: 512px; height: 1041px; }

  .brand {
    position: absolute; left: 0; right: 0; top: 0; height: 147px;
    display: flex; align-items: center; justify-content: center; gap: 12px;
  }
  .brand__mark { width: 14px; height: 14px; background: var(--text); }
  .brand__name {
    font-family: "Roboto", sans-serif; font-weight: 400; font-size: 22px;
    letter-spacing: 0.5px; color: var(--text); text-transform: uppercase;
  }

  .photo-grid { position: absolute; top: 147px; left: 0; right: 0; }
  .photo { position: absolute; overflow: hidden; }

  .offer {
    position: absolute; left: 0; right: 0; bottom: 0;
    padding: 40px 18px 16px;
    background: linear-gradient(180deg, rgba(0,0,0,0) 0%, var(--caption-shade) 55%);
    font-weight: 300; font-size: 13px; line-height: 18px; color: var(--text);
  }
  .offer__title {
    font-weight: 400; font-size: 14px; letter-spacing: 1px;
    text-transform: uppercase; margin-bottom: 4px;
  }
  .offer__list { list-style: none; }

  .headline {
    position: absolute; left: 50px; top: 707px;
    font-weight: 300; font-size: 49px; line-height: 58px; letter-spacing: 0.5px;
    text-transform: uppercase;
  }
  .intro {
    position: absolute; left: 50px; top: 843px; width: 430px;
    font-family: "Fira Sans Condensed", sans-serif; font-style: italic; font-weight: 400;
    font-size: 17.5px; line-height: 21.5px; color: var(--text);
  }
  .contact {
    position: absolute; left: 50px; top: 945px; font-style: normal;
    font-weight: 300; font-size: 13.5px; line-height: 17px; color: var(--text-soft);
    white-space: nowrap;
  }
  .flyer--back .contact { top: 946px; }
</style>
</head>
<body>

<section class="flyer flyer--front">
  <header class="brand">
    <span class="brand__mark"></span>
    <span class="brand__name">Bar Velluto</span>
  </header>

  <div class="photo-grid">
    <div class="photo" role="img" aria-label="Gin Tonic im Ballonglas mit Zitronenzeste und Eis auf dunklem Tisch mit Wacholderbeeren und Rosmarin"
      style="left:0; top:0; width:259px; height:521px;
      background:
        radial-gradient(ellipse 70px 95px at 52% 38%, #e9eef1 0%, #b9c3c8 45%, rgba(120,128,132,0) 100%),
        linear-gradient(180deg, #141414 0%, #1c1c1c 70%, #3a3836 82%, #1a1918 100%);"></div>
    <div class="photo" role="img" aria-label="Grüner Smoothie im Glas mit Kiwischeiben, Orange und Spinat auf hellem Holz"
      style="left:259px; top:0; width:259px; height:521px;
      background:
        radial-gradient(circle 70px at 30% 12%, #f6a21e 0%, #f0b040 60%, rgba(240,176,64,0) 100%),
        radial-gradient(ellipse 110px 140px at 50% 58%, #2f7a16 0%, #4f9a2a 60%, rgba(79,154,42,0) 100%),
        linear-gradient(170deg, #6aa83a 0%, #8cc04c 40%, #b8d49a 75%, #eef0e6 100%);">
      <div class="offer">
        <p class="offer__title">Smoothie Bar</p>
        <ul class="offer__list">
          <li>Grün · fruchtig · Superfood</li>
          <li>detox · Bio</li>
        </ul>
      </div>
    </div>
  </div>

  <div class="offer" style="position:absolute; top:538px; left:0; width:259px; bottom:auto; height:130px; padding-top:20px;">
    <p class="offer__title">Cocktailbar</p>
    <ul class="offer__list">
      <li>Klassisch · Cocktail LAB</li>
      <li>Caipirinha Bar</li>
      <li>Cocktail Workshop · Bio Cocktails</li>
    </ul>
  </div>

  <h1 class="headline">Für jedes Event<br>das Richtige</h1>
  <p class="intro">Ob privat oder geschäftlich, innen oder außen, groß oder<br>klein - wir garantieren Ihnen ein Highlight auf jeder<br>Veranstaltung zu sein.</p>
  <address class="contact">
    Bar Velluto &nbsp;|&nbsp; Am Lindenhain 12 &nbsp;|&nbsp; 90411 Nürnberg<br>
    Tel: 0911 48213 907 &nbsp;|&nbsp; info@bar-velluto.de<br>
    www.bar-velluto.de
  </address>
</section>

<section class="flyer flyer--back">
  <header class="brand">
    <span class="brand__mark"></span>
    <span class="brand__name">Bar Velluto</span>
  </header>

  <div class="photo-grid">
    <div class="photo" role="img" aria-label="Bernsteinfarbener Cocktail im Kristallglas mit getrockneter Orangenscheibe auf dunklem Tablett"
      style="left:0; top:0; width:255px; height:253px;
      background:
        radial-gradient(ellipse 52px 62px at 47% 42%, #e29a4a 0%, #b8662a 55%, rgba(120,60,25,0) 100%),
        linear-gradient(180deg, #1d0f0c 0%, #2a1712 65%, #3a2a24 78%, #120c0a 100%);"></div>
    <div class="photo" role="img" aria-label="Grüne Smoothies in Glas und Flasche mit Limetten auf Holztisch"
      style="left:255px; top:0; width:257px; height:253px;
      background:
        radial-gradient(ellipse 48px 60px at 52% 55%, #8fb23c 0%, #6f9a2c 60%, rgba(111,154,44,0) 100%),
        radial-gradient(ellipse 30px 75px at 75% 30%, #7ea83a 0%, rgba(126,168,58,0) 100%),
        linear-gradient(180deg, #ecebe8 0%, #dcdbd6 45%, #6b5a48 60%, #3a3430 100%);"></div>
    <div class="photo" role="img" aria-label="Goldgelber Cocktail mit Eis und Fruchtchip, daneben Apfel und rote Pfefferbeeren"
      style="left:0; top:253px; width:255px; height:254px;
      background:
        radial-gradient(ellipse 55px 70px at 55% 47%, #f0b63c 0%, #c57a1c 55%, rgba(120,70,20,0) 100%),
        radial-gradient(circle 32px at 18% 38%, #8a2a22 0%, rgba(90,30,20,0) 100%),
        linear-gradient(180deg, #0f0d0c 0%, #141110 70%, #2a2420 85%, #111 100%);"></div>
    <div class="photo" role="img" aria-label="Beeren-Smoothie-Bowl auf rosa Teller zwischen grünen Blättern"
      style="left:255px; top:253px; width:257px; height:254px;
      background:
        radial-gradient(circle 48px at 50% 42%, #c98ab6 0%, #b67aa6 70%, rgba(230,200,200,0) 100%),
        radial-gradient(circle 100px at 55% 45%, #ecd1cc 0%, #e6c6c2 60%, rgba(230,198,194,0) 100%),
        linear-gradient(160deg, #2f5a2e 0%, #3f7040 50%, #24442a 100%);"></div>
    <div class="photo" role="img" aria-label="Moscow Mule im Kupferbecher mit Gurke und Ingwer auf dunklem Tisch"
      style="left:0; top:507px; width:255px; height:253px;
      background:
        radial-gradient(ellipse 45px 60px at 50% 52%, #b07a4e 0%, #8a5a36 60%, rgba(90,55,35,0) 100%),
        linear-gradient(180deg, #2a1e1a 0%, #3a2a24 55%, #1e1512 75%, #0e0a08 100%);"></div>
    <div class="photo" role="img" aria-label="Rosa Smoothie im Glas mit Ananas, Bananen, Erdbeeren und Orangen vor rosa Wand"
      style="left:255px; top:507px; width:257px; height:253px;
      background:
        radial-gradient(ellipse 28px 40px at 60% 66%, #f2a7b4 0%, rgba(242,167,180,0) 100%),
        radial-gradient(ellipse 34px 70px at 76% 40%, #b0862c 0%, rgba(176,134,44,0) 100%),
        linear-gradient(180deg, #e6cdcc 0%, #e2c4c2 62%, #f4f1ec 63%, #ffffff 100%);"></div>
  </div>

  <address class="contact">
    Bar Velluto &nbsp;|&nbsp; Am Lindenhain 12 &nbsp;|&nbsp; 90411 Nürnberg<br>
    Tel: 0911 48213 907 &nbsp;|&nbsp; info@bar-velluto.de<br>
    www.bar-velluto.de
  </address>
</section>

</body>
</html>
```